Veltrion Knowledge Enhancement Company Website

Veltrion is knowledge enhancement Highend and Deep Technology Company who has training programs in Applied Quantum, Applied Artificial Intelligence and Data Science. All the technologies are very advanced and future technologies and the website should reflect the technology advancement. Looking for a sophisticated web design which will reflect our focus on deep and future technologies. Logo file is uploaded

Target Market(s)

Big Corporates and Premium Colleges

Industry/Entity Type

Technology, Deep Technology, Future Technology

Coding

Coded - Design and coding required

Number of Pages Required

5+ page

Requirements
Must have
• A Very Contemporary clean look and should reflect Future Technologies
Nice to have
• Should be very Classy
Should not have
• Traditional Fonts and Colors

```html
<!DOCTYPE html>
<html lang="en">
<head>
<meta charset="utf-8">
<title>Veltrion — Knowledge Enhancement</title>
<link rel="stylesheet" href="https://fonts.googleapis.com/css2?family=Marcellus&family=Poppins:wght@400;500;600&display=swap">
<style>
:root{
  --blue:#1fa0de;
  --blue-soft:#8fd0f0;
  --ink:#0d0d26;
  --text:#555a66;
  --muted:#8b909a;
  --tint:#f3f9fd;
  --hero:#f4f9fe;
  --navy:#0a1433;
  --white:#ffffff;
}
*{box-sizing:border-box;margin:0;padding:0}
html,body{width:1200px;height:3728px;overflow:hidden}
body{font-family:"Poppins",sans-serif;color:var(--ink);background:var(--white);position:relative}
.section{position:absolute;left:0;width:1200px}
.abs{position:absolute}
.serif{font-family:"Marcellus",serif;font-weight:400}
.brand{font-family:"Poppins",sans-serif;font-weight:600;color:var(--blue);font-size:26px;display:flex;align-items:center;gap:10px}
.brand-square{width:22px;height:22px;background:var(--blue)}
.nav{display:flex;font-size:15px;color:var(--ink)}
.nav a{color:inherit;text-decoration:none;position:absolute;white-space:nowrap}
.nav a.active{color:var(--blue)}
.eyebrow{font-size:16px;font-weight:500;color:var(--blue);letter-spacing:1px}
.heading{font-family:"Marcellus",serif;font-size:35px;line-height:45px;color:var(--ink)}
.copy{font-size:14px;line-height:23px;color:var(--text)}
.btn{display:flex;align-items:center;justify-content:center;background:var(--blue);color:var(--white);font-size:15px;clip-path:polygon(12px 0,100% 0,100% 100%,0 100%);}
.art{border-radius:24px}
.diamond{position:absolute;width:28px;height:28px;background:var(--blue-soft);transform:rotate(45deg);opacity:.8}
.program-icon{width:56px;height:56px}
.program-title{font-size:19px;font-weight:500;color:var(--ink);white-space:nowrap}
.program-copy{font-size:13.5px;line-height:24.5px;color:var(--muted)}
.checks li{list-style:none;display:flex;align-items:center;gap:10px;font-size:14px;color:var(--ink);height:33px}
.card{position:absolute;top:2895px;width:278px;height:434px;background:var(--white);border-radius:0 0 22px 22px;box-shadow:0 10px 24px rgba(20,60,120,.08);overflow:hidden}
.card-img{height:203px}
.card-body{padding:22px 20px 0 22px}
.card-date{font-size:12px;color:var(--muted)}
.card-title{font-size:16px;font-weight:500;line-height:23px;margin-top:12px}
.card-copy{font-size:11.5px;line-height:19px;color:var(--muted);margin-top:10px}
.card-link{font-size:13px;color:var(--blue);margin-top:12px;display:flex;align-items:center;gap:8px}
.footer{background:var(--navy);color:var(--white)}
.footer .nav{color:var(--white)}
.contact{display:flex;gap:14px;align-items:center;font-size:14px;line-height:22px}
.social{display:flex;gap:13px}
.social span{width:24px;height:24px;border-radius:50%;background:var(--blue)}
</style>
</head>
<body>

<!-- Hero -->
<header class="section" style="top:0;height:593px;background:linear-gradient(180deg,#fbfdff,var(--hero))">
  <div class="brand abs" style="left:162px;top:50px"><span class="brand-square"></span>Veltrion</div>
  <nav class="nav">
    <a class="active" style="left:541px;top:43px">Home</a>
    <a style="left:634px;top:43px">About Us</a>
    <a style="left:753px;top:43px">Program</a>
    <a style="left:868px;top:43px">News</a>
    <a style="left:957px;top:43px">Contact Us</a>
  </nav>
  <p class="abs" style="left:163px;top:243px;font-size:19px;color:var(--blue)">Applying Data Science</p>
  <h1 class="heading abs" style="left:162px;top:278px;font-size:36px;line-height:48px">And Techniques with<br>Systems</h1>
  <a class="btn abs" style="left:169px;top:398px;width:150px;height:45px">Contect Us</a>
  <div class="art abs" role="img" aria-label="Isometric illustration of server stacks and a laptop connected by glowing data lines" style="left:547px;top:123px;width:539px;height:427px;background:radial-gradient(ellipse at center,#cfe6fb 0%,#e6f1fd 55%,rgba(244,249,254,0) 75%)"></div>
</header>

<!-- About -->
<section class="section" style="top:593px;height:666px">
  <span class="diamond" style="left:56px;top:30px"></span>
  <span class="diamond" style="left:-12px;top:96px"></span>
  <span class="diamond" style="left:30px;top:358px"></span>
  <span class="diamond" style="left:1112px;top:574px"></span>
  <div class="art abs" role="img" aria-label="Isometric illustration of people working beside server racks, a cloud and a laptop" style="left:87px;top:102px;width:449px;height:477px;background:linear-gradient(160deg,#e2effc,#c9ddf6)"></div>
  <p class="eyebrow abs" style="left:609px;top:156px">ABOUT US</p>
  <h2 class="heading abs" style="left:609px;top:182px">Veltrion Technology<br>Training</h2>
  <div class="copy abs" style="left:610px;top:289px;width:432px;text-align:justify">
    <p>Quantum computing could be the most significant technological revolution since the internet's inception. According to experts, the market for quantum technologies will quadruple by 2029. There has never been a better time to get involved in a thriving industry like quantum computing.</p>
    <p style="margin-top:12px">Quantum technology will necessitate far more than project managers and theoretical physicists.</p>
  </div>
  <a class="btn abs" style="left:620px;top:493px;width:137px;height:37px">Read More</a>
</section>

<!-- Program -->
<section class="section" style="top:1259px;height:471px;background:var(--tint)">
  <p class="eyebrow abs" style="left:162px;top:95px">PROGRAM</p>
  <h2 class="heading abs" style="left:162px;top:118px">Our Training Program</h2>
  <p class="copy abs" style="left:613px;top:96px;width:430px">Lorem ipsum dolor sit amet, consectetur adipiscing elit. itempor lacus, sit amet fringilla neque. Aliquam vel porta erat. ano neque Suspendisse ut vehicula ex.</p>

  <svg class="program-icon abs" style="left:162px;top:196px" viewBox="0 0 56 56" fill="none" stroke="#0d0d26" stroke-width="2">
    <rect x="8" y="8" width="40" height="40" rx="2"/>
    <ellipse cx="28" cy="28" rx="13" ry="5" stroke="#1fa0de"/>
    <ellipse cx="28" cy="28" rx="13" ry="5" stroke="#1fa0de" transform="rotate(60 28 28)"/>
    <ellipse cx="28" cy="28" rx="13" ry="5" stroke="#1fa0de" transform="rotate(-60 28 28)"/>
    <path d="M16 2v6M24 2v6M32 2v6M40 2v6M16 48v6M24 48v6M32 48v6M40 48v6M2 16h6M2 24h6M2 32h6M2 40h6M48 16h6M48 24h6M48 32h6M48 40h6"/>
  </svg>
  <p class="program-title abs" style="left:163px;top:277px">Applied Quantum</p>
  <p class="program-copy abs" style="left:163px;top:308px;width:232px">Lorem ipsum dolor sit amet, elit consectetuer elit adipiscing ie no Lorem ipsum dolor sit amet consectetuer adipiscing .</p>

  <svg class="program-icon abs" style="left:460px;top:196px" viewBox="0 0 56 56" fill="none" stroke="#0d0d26" stroke-width="2">
    <circle cx="28" cy="28" r="10" stroke="#1fa0de"/>
    <text x="28" y="32" font-size="10" text-anchor="middle" fill="#1fa0de" stroke="none" font-family="Poppins,sans-serif">AI</text>
    <path d="M28 18V6M28 38v12M18 28H6M38 28h12M21 21l-9-9M35 21l9-9M21 35l-9 9M35 35l9 9"/>
    <circle cx="28" cy="4" r="2.5"/><circle cx="28" cy="52" r="2.5"/><circle cx="4" cy="28" r="2.5"/><circle cx="52" cy="28" r="2.5"/>
    <circle cx="10" cy="10" r="2.5"/><circle cx="46" cy="10" r="2.5"/><circle cx="10" cy="46" r="2.5"/><circle cx="46" cy="46" r="2.5"/>
  </svg>
  <p class="program-title abs" style="left:463px;top:279px">Applied Artificial Intelligence</p>
  <p class="program-copy abs" style="left:463px;top:310px;width:262px;text-align:justify">Lorem ipsum dolor sit fringilla amet, consectetur adipiscing ipsum neque elit. Pellentesque in tempor it lacus, amet &nbsp;sit amet fringilla neque.</p>

  <svg class="program-icon abs" style="left:813px;top:196px" viewBox="0 0 56 56" fill="none" stroke="#0d0d26" stroke-width="2">
    <ellipse cx="28" cy="14" rx="11" ry="4" stroke="#1fa0de"/>
    <path d="M17 14v28c0 2 5 4 11 4s11-2 11-4V14M17 23c0 2 5 4 11 4s11-2 11-4M17 32c0 2 5 4 11 4s11-2 11-4" stroke="#1fa0de"/>
    <path d="M17 20H6V8M39 20h11V8M17 36H6v12M39 36h11v12"/>
    <circle cx="6" cy="6" r="2.5"/><circle cx="50" cy="6" r="2.5"/><circle cx="6" cy="50" r="2.5"/><circle cx="50" cy="50" r="2.5"/>
  </svg>
  <p class="program-title abs" style="left:815px;top:279px">Data Science</p>
  <p class="program-copy abs" style="left:815px;top:308px;width:232px">Lorem ipsum dolor sit amet, elit consectetuer elit adipiscing ie no Lorem ipsum dolor sit amet consectetuer adipiscing .</p>
</section>

<!-- Feature -->
<section class="section" style="top:1730px;height:603px">
  <span class="diamond" style="left:76px;top:476px"></span>
  <span class="diamond" style="left:12px;top:541px"></span>
  <p class="eyebrow abs" style="left:162px;top:106px">LOREM IPSUM</p>
  <h2 class="heading abs" style="left:162px;top:132px">Lorem ipsum dolor sit amet,<br>consectetur</h2>
  <p class="copy abs" style="left:164px;top:238px;width:434px">Lorem ipsum dolor amet nosit amet, consectetur adipiscing elit. Pellentesque in tempor lacus, sit amet fringilla neque. Aliquam vel porta erat. Suspendisse ut vehicula ex.</p>
  <ul class="checks abs" style="left:162px;top:316px">
    <li><svg width="16" height="16" viewBox="0 0 16 16"><circle cx="8" cy="8" r="8" fill="#1fa0de"/><path d="M4.5 8.2l2.3 2.3 4.7-4.9" stroke="#fff" stroke-width="1.8" fill="none"/></svg>Lorem ipsum dolor sit , consectetur adipiscing elit.</li>
    <li><svg width="16" height="16" viewBox="0 0 16 16"><circle cx="8" cy="8" r="8" fill="#1fa0de"/><path d="M4.5 8.2l2.3 2.3 4.7-4.9" stroke="#fff" stroke-width="1.8" fill="none"/></svg>Sed nec suscipit sapien, eu no tempor non &nbsp;lectus.</li>
    <li><svg width="16" height="16" viewBox="0 0 16 16"><circle cx="8" cy="8" r="8" fill="#1fa0de"/><path d="M4.5 8.2l2.3 2.3 4.7-4.9" stroke="#fff" stroke-width="1.8" fill="none"/></svg>Duis tincidunt elementum ligula, non lacinia mi vel.</li>
  </ul>
  <a class="btn abs" style="left:169px;top:450px;width:138px;height:36px">Read More</a>
  <div class="art abs" role="img" aria-label="Isometric illustration of a person on a large laptop with charts and bar graphs" style="left:644px;top:72px;width:456px;height:442px;background:linear-gradient(160deg,#e3eefb,#c7daf3)"></div>
</section>

<!-- Call to action -->
<section class="section" style="top:2333px;height:355px;background:linear-gradient(100deg,#2aa7e2,#1b9ad8)">
  <h2 class="serif abs" style="left:0;width:1200px;top:96px;text-align:center;font-size:35px;color:var(--white)">Get Ready to StartYour Project With Us</h2>
  <p class="abs" style="left:250px;width:700px;top:150px;text-align:center;font-size:14px;line-height:21px;color:var(--white)">Lorem ipsum dolor sit amet, consectetur adipiscing elit. Pellentesque in tempor lacus, sit amet fringilla neque. Aliquam vel porta erat. Suspendisse ut vehicula ex. Duis tincidunt elementum ligula.</p>
  <a class="btn abs" style="left:537px;top:225px;width:138px;height:37px;background:var(--white);color:var(--blue)">Contact Us</a>
</section>

<!-- News -->
<section class="section" style="top:2688px;height:731px">
  <span class="diamond" style="left:1090px;top:608px"></span>
  <span class="diamond" style="left:1154px;top:670px"></span>
  <p class="eyebrow abs" style="left:162px;top:103px">NEWS</p>
  <h2 class="heading abs" style="left:162px;top:127px">Recent Blogs And News</h2>
  <p class="copy abs" style="left:613px;top:98px;width:430px">Lorem ipsum dolor sit amet, consectetur adipiscing elit. itempor lacus, sit amet fringilla neque. Aliquam vel porta erat. ano neque Suspendisse ut vehicula ex.</p>
</section>

<article class="card" style="left:162px">
  <div class="card-img" role="img" aria-label="Photo of a glowing AI circuit board" style="background:linear-gradient(135deg,#3a1f6e,#1b2f7a 55%,#0e1b4d)"></div>
  <div class="card-body">
    <p class="card-date">13/01/2022— Mara K.</p>
    <h3 class="card-title">Lorem Ipsum Dolor Sit Amet<br>Con Se Ctetuer Adipis.</h3>
    <p class="card-copy">sed diam nonummy it mnibh euismod tinci dunt ut it no looreet dolore magna aliquam erat volutpat Ut wisi ad.</p>
    <p class="card-link">Read More <svg width="16" height="8" viewBox="0 0 16 8"><path d="M0 4h14M11 1l3 3-3 3" stroke="#1fa0de" stroke-width="1.6" fill="none"/></svg></p>
  </div>
</article>
<article class="card" style="left:462px">
  <div class="card-img" role="img" aria-label="Photo of a lit data centre corridor" style="background:linear-gradient(180deg,#0fb7c9,#0a4f6e 55%,#1a1436)"></div>
  <div class="card-body">
    <p class="card-date">13/01/2022— Mara K.</p>
    <h3 class="card-title">Lorem Ipsum Dolor Sit Amet<br>Con Se Ctetuer Adipis.</h3>
    <p class="card-copy">sed diam nonummy it mnibh euismod tinci dunt ut it no looreet dolore magna aliquam erat volutpat Ut wisi ad.</p>
    <p class="card-link">Read More <svg width="16" height="8" viewBox="0 0 16 8"><path d="M0 4h14M11 1l3 3-3 3" stroke="#1fa0de" stroke-width="1.6" fill="none"/></svg></p>
  </div>
</article>
<article class="card" style="left:761px">
  <div class="card-img" role="img" aria-label="Photo of a digital globe with network lines" style="background:radial-gradient(circle at 30% 50%,#2d7fd8,#0d2a78 55%,#070f3a)"></div>
  <div class="card-body">
    <p class="card-date">13/01/2022— Mara K.</p>
    <h3 class="card-title">Lorem Ipsum Dolor Sit Amet<br>Con Se Ctetuer Adipis.</h3>
    <p class="card-copy">sed diam nonummy it mnibh euismod tinci dunt ut it no looreet dolore magna aliquam erat volutpat Ut wisi ad.</p>
    <p class="card-link">Read More <svg width="16" height="8" viewBox="0 0 16 8"><path d="M0 4h14M11 1l3 3-3 3" stroke="#1fa0de" stroke-width="1.6" fill="none"/></svg></p>
  </div>
</article>

<!-- Footer -->
<footer class="section footer" style="top:3419px;height:309px">
  <div class="brand abs" style="left:162px;top:62px"><span class="brand-square"></span>Veltrion</div>
  <nav class="nav">
    <a style="left:541px;top:61px">Home</a>
    <a style="left:634px;top:61px">About Us</a>
    <a style="left:753px;top:61px">Program</a>
    <a style="left:868px;top:61px">News</a>
    <a style="left:957px;top:61px">Contact Us</a>
  </nav>
  <div class="abs" style="left:162px;top:134px;width:877px;height:1px;background:rgba(255,255,255,.12)"></div>
  <div class="contact abs" style="left:162px;top:164px">
    <svg width="34" height="38" viewBox="0 0 34 38" fill="none" stroke="#1fa0de" stroke-width="2"><path d="M17 30s-10-10-10-17a10 10 0 0 1 20 0c0 7-10 17-10 17z"/><circle cx="17" cy="13" r="4"/><path d="M4 30c-3 4 26 8 26 2"/></svg>
    <span>123, building name, street City,<br>State XY 123456</span>
  </div>
  <div class="contact abs" style="left:518px;top:164px">
    <svg width="34" height="38" viewBox="0 0 34 38" fill="none" stroke="#1fa0de" stroke-width="2"><path d="M8 8l6 6-3 4c2 4 5 7 9 9l4-3 6 6-4 4C14 34 4 24 4 12z"/><path d="M20 6a10 10 0 0 1 10 10M20 11a5 5 0 0 1 5 5"/></svg>
    <span>Phone<br>+ 1 123 456 7890</span>
  </div>
  <div class="contact abs" style="left:805px;top:164px">
    <svg width="34" height="38" viewBox="0 0 34 38" fill="none" stroke="#1fa0de" stroke-width="2"><path d="M3 16l14-11 14 11v18H3z"/><path d="M3 16l14 10 14-10"/><path d="M9 12V6h16v6"/></svg>
    <span><b style="font-weight:500">E-Mail</b><br>hello@veltrion-learn.com</span>
  </div>
  <p class="abs" style="left:162px;top:255px;font-size:14px">© 2023 Veltrion. All Rights Reserved.</p>
  <div class="social abs" style="left:906px;top:258px"><span></span><span></span><span></span><span></span></div>
</footer>

</body>
</html>
```